Online eyewear company needs a couple Sign-In and Product Review page designs

We sell prescription glasses starting at $99 with Free Shipping. We have over 300 different styles and colors.Our website is under construction and we need an amazing Sign-In and Product Review Pages to help finish things off. Our brand is called VESKA and our website is called VESKAEYEWEAR.COM.

We need 5 simple sign-in and product review pages to help finish our website. Sample pages attached

We need the pages to go in order

Quick Checkout review
Sign-In
Prescription
Shipping & Payment
Final Review

Target Market(s)

20-50 that wears glasses

Industry/Entity Type

Eyewear

Colors
ffffff
919191
eaeaea
d3d3d3
dddddd
b7b7b7
000000
3176b5

Requirements
Must have
• Simple, creative, original. Must not be exactly like the photos attached. They're just templete of our casual, simple style.
• We need the pages to go in order
• Quick Checkout review
• Sign-In
• Prescription
• Shipping & Payment
• Final Review
Should not have
• Must not look exactly like the photos attached.

```html
<!DOCTYPE html>
<html lang="en">
<head>
<meta charset="utf-8">
<title>VESKA — Your Cart</title>
<link rel="stylesheet" href="https://fonts.googleapis.com/css2?family=Open+Sans:ital,wght@0,300;0,400;0,600;0,700;1,400&display=swap">
<style>
  :root {
    --white: #ffffff;
    --ink: #000000;
    --text: #4a4a4a;
    --muted: #919191;
    --band: #eaeaea;
    --rule: #d3d3d3;
    --panel: #eaeaea;
    --soft: #dddddd;
    --line: #b7b7b7;
    --brand: #3176b5;
    --footer: #3b3b3b;
    --footer-deep: #2c2c2c;
    --badge: #d4127a;
  }
  * { box-sizing: border-box; margin: 0; padding: 0; }
  html, body { width: 1200px; height: 1015px; overflow: hidden; }
  body { position: relative; background: var(--white); color: var(--text); font-family: "Open Sans", Arial, sans-serif; }
  .abs { position: absolute; }

  .promo-band { left: 0; top: 0; width: 1200px; height: 31px; background: var(--band); font-size: 10px; color: #222; text-align: center; line-height: 31px; letter-spacing: -0.2px; }
  .site-header { left: 0; top: 31px; width: 1200px; height: 57px; border-bottom: 1px solid var(--rule); }
  .brand-name { left: 90px; top: 40px; font-size: 22px; font-weight: 300; letter-spacing: 3px; color: #111; }
  .main-nav { left: 281px; top: 50px; display: flex; gap: 19px; font-size: 13px; color: #222; letter-spacing: -0.3px; }
  .utility-nav { left: 1028px; top: 53px; display: flex; align-items: center; gap: 8px; font-size: 11.5px; color: #555; }
  .utility-nav .sep { color: var(--brand); }
  .cart-button { left: 1150px; top: 11px; width: 33px; height: 36px; border-radius: 7px; background: var(--white); box-shadow: 0 1px 4px rgba(0,0,0,.35); display: flex; align-items: center; justify-content: center; }
  .cart-badge { left: 1141px; top: 4px; width: 16px; height: 16px; border-radius: 50%; background: var(--badge); color: var(--white); font-size: 8px; text-align: center; line-height: 16px; }

  .cart-title { left: 250px; top: 129px; font-size: 16px; color: #666; }
  .update-cart { left: 870px; top: 127px; width: 80px; height: 20px; background: var(--brand); color: var(--white); font-size: 10.5px; font-weight: 600; text-align: center; line-height: 20px; }
  .cart-head { left: 250px; top: 191px; width: 708px; height: 21px; border-bottom: 1px solid var(--soft); font-size: 10.5px; color: #444; }
  .cart-head span { position: absolute; top: 0; }
  .divider { left: 250px; width: 708px; height: 1px; background: var(--soft); }

  .frame-photo { width: 162px; height: 52px; border-radius: 20px 20px 26px 26px; background: linear-gradient(180deg, #f4efec 0%, #e3d8d2 55%, #f4efec 100%); }
  .product-name { left: 439px; top: 244px; font-size: 16px; color: #555; }
  .spec { font-size: 7.5px; line-height: 9.4px; color: #555; }
  .spec-label { left: 441px; font-weight: 600; }
  .spec-colon { left: 513px; }
  .spec-value { left: 537px; font-style: italic; }
  .money { font-size: 13px; color: #444; }
  .qty { width: 30px; height: 20px; border: 1px solid var(--soft); font-size: 10px; color: #333; padding-left: 7px; line-height: 18px; }
  .qty svg { position: absolute; right: 2px; top: 2px; }
  .row-icons { display: flex; gap: 14px; }

  .order-summary { left: 247px; top: 588px; width: 403px; height: 130px; background: var(--panel); }
  .summary-title { left: 258px; top: 596px; font-size: 17px; font-weight: 600; color: #555; }
  .summary-row { left: 275px; width: 346px; font-size: 10.5px; color: #666; display: flex; justify-content: space-between; }
  .summary-row b { font-weight: 600; color: #444; font-size: 10px; }
  .summary-rule { left: 273px; top: 677px; width: 358px; height: 1px; background: #999; }
  .summary-total { left: 275px; top: 688px; width: 346px; font-size: 16px; font-weight: 600; color: #555; display: flex; justify-content: space-between; }
  .checkout-button { left: 672px; top: 589px; width: 283px; height: 62px; background: var(--brand); color: var(--white); font-size: 16px; font-weight: 600; text-align: center; line-height: 62px; }
  .checkout-note { left: 672px; top: 661px; width: 283px; font-size: 7.5px; font-style: italic; color: #555; text-align: center; }

  .site-footer { left: 0; top: 809px; width: 1200px; height: 206px; background: radial-gradient(ellipse at 50% 40%, #4a4a4a 0%, var(--footer) 45%, var(--footer-deep) 100%); }
  .footer-brand { left: 251px; top: 848px; font-size: 36px; font-weight: 300; letter-spacing: 6px; color: var(--white); }
  .footer-col { top: 854px; color: #e6e6e6; }
  .footer-col h3 { font-size: 14px; font-weight: 700; color: var(--white); letter-spacing: -0.6px; margin-bottom: 9px; }
  .footer-col li { list-style: none; font-size: 12.5px; line-height: 22px; color: #dcdcdc; }
</style>
</head>
<body>
  <div class="abs promo-band">FREE SHIPPING IN CONTINENTAL US</div>
  <header class="abs site-header"></header>
  <div class="abs brand-name">VESKA</div>
  <nav class="abs main-nav"><span>EYEGLASSES</span><span>ORDER LENSES</span></nav>
  <div class="abs utility-nav">
    <svg width="13" height="13" viewBox="0 0 13 13"><circle cx="5.5" cy="5.5" r="4.2" fill="none" stroke="#aaa" stroke-width="1.6"/><line x1="8.6" y1="8.6" x2="12" y2="12" stroke="#aaa" stroke-width="1.8"/></svg>
    <span>SEARCH</span><span class="sep">|</span><span>HELP</span>
  </div>
  <div class="abs cart-button">
    <svg width="20" height="16" viewBox="0 0 20 16"><path d="M1 6h18l-2 9H3z" fill="#111"/><path d="M6 6l4-5 4 5" fill="none" stroke="#111" stroke-width="1.6"/></svg>
  </div>
  <div class="abs cart-badge">2</div>

  <main>
    <h1 class="abs cart-title" style="font-weight:400">Your Cart (2) Items</h1>
    <div class="abs update-cart">Update Cart</div>
    <div class="abs cart-head">
      <span style="left:1px">Item</span>
      <span style="left:438px">Price</span>
      <span style="left:556px">Qty</span>
      <span style="left:643px">SubTotal</span>
    </div>

    <!-- Frame line item -->
    <div class="abs frame-photo" style="left:248px;top:268px" role="img" aria-label="Brown metal cat-eye eyeglass frame, front view"></div>
    <h2 class="abs product-name" style="font-weight:400">Wrenfield</h2>
    <div class="abs spec spec-label" style="top:275px">Dimensions<br>Shape<br>Size<br>Material<br>Color</div>
    <div class="abs spec spec-colon" style="top:275px">:<br>:<br>:<br>:<br>:</div>
    <div class="abs spec spec-value" style="top:275px">53 × 17 × 138 cm<br>Cat-eye, Square<br>Medium<br>Metal<br>Brown</div>
    <div class="abs money" style="left:684px;top:285px">$99.00</div>
    <div class="abs qty" style="left:800px;top:282px">1<svg width="6" height="14" viewBox="0 0 6 14"><path d="M0 5l3-3 3 3M0 9l3 3 3-3" fill="none" stroke="#888" stroke-width="0.9"/></svg></div>
    <div class="abs money" style="left:894px;top:285px">$99.00</div>
    <div class="abs row-icons" style="left:887px;top:337px">
      <svg width="16" height="17" viewBox="0 0 16 17"><path d="M3 14l1-4 8-8 3 3-8 8z M4 10l3 3" fill="none" stroke="#666" stroke-width="1"/></svg>
      <svg width="15" height="18" viewBox="0 0 15 18"><path d="M1 3h13M5 3V1h5v2M3 3l1 14h7l1-14M6 6v9M9 6v9" fill="none" stroke="#666" stroke-width="1"/></svg>
    </div>
    <div class="abs divider" style="top:372px"></div>

    <!-- Lens line item -->
    <div class="abs frame-photo" style="left:250px;top:433px" role="img" aria-label="Brown metal eyeglass frame fitted with prescription lenses"></div>
    <div class="abs spec spec-label" style="top:434px">Lens<br>Perscription type<br>Lens type<br>Lens Thickness</div>
    <div class="abs spec spec-colon" style="top:434px">:<br>:<br>:<br>:</div>
    <div class="abs spec spec-value" style="top:433px">Rx Lenses<br>Single vision Lens<br>Computer Lenses<br>Polycarbonate Lens</div>
    <div class="abs money" style="left:677px;top:438px">$253.00</div>
    <div class="abs qty" style="left:800px;top:438px">1<svg width="6" height="14" viewBox="0 0 6 14"><path d="M0 5l3-3 3 3M0 9l3 3 3-3" fill="none" stroke="#888" stroke-width="0.9"/></svg></div>
    <div class="abs money" style="left:887px;top:438px">$253.00</div>
    <div class="abs row-icons" style="left:887px;top:499px">
      <svg width="16" height="17" viewBox="0 0 16 17"><path d="M3 14l1-4 8-8 3 3-8 8z M4 10l3 3" fill="none" stroke="#666" stroke-width="1"/></svg>
      <svg width="15" height="18" viewBox="0 0 15 18"><path d="M1 3h13M5 3V1h5v2M3 3l1 14h7l1-14M6 6v9M9 6v9" fill="none" stroke="#666" stroke-width="1"/></svg>
    </div>
    <div class="abs divider" style="top:530px"></div>

    <!-- Summary -->
    <section class="abs order-summary"></section>
    <h2 class="abs summary-title">Order Summary</h2>
    <div class="abs summary-row" style="top:630px"><span>SUB TOTAL &nbsp;(2) Items</span><b>$352</b></div>
    <div class="abs summary-row" style="top:656px"><span>SHIPPING FEE</span><b>FREE</b></div>
    <div class="abs summary-rule"></div>
    <div class="abs summary-total"><span>TOTAL</span><span>$352</span></div>

    <div class="abs checkout-button">Proceed to Checkout</div>
    <p class="abs checkout-note">Free of Standard Shipping (CONTINENTAL US) and free return on all orders.</p>
  </main>

  <footer class="abs site-footer" role="img" aria-label="Dark backdrop with a faint close-up of clear eyeglass frames"></footer>
  <div class="abs footer-brand">VESKA</div>
  <div class="abs footer-col" style="left:457px">
    <h3>PRODUCTS</h3>
    <ul><li>Men’s Frames</li><li>Women’s Frames</li><li>New Arrivals</li><li>Best Sellers</li><li>Featured Frames</li></ul>
  </div>
  <div class="abs footer-col" style="left:635px">
    <h3>ORDER</h3>
    <ul><li>Single Vision Lenses</li><li>Blue Light Blocking</li><li>Computer Lenses</li><li>High Index Lenses</li><li>Transition Lenses</li><li>Reading Lenses</li></ul>
  </div>
  <div class="abs footer-col" style="left:814px">
    <h3>INFORMATION</h3>
    <ul><li>Track Order</li><li>About Us</li><li>Contact Us</li><li>Returns</li><li>Warranty</li><li>FAQ</li></ul>
  </div>
</body>
</html>
```